I have an existing corporate logo. I'd like to clean it up bit (sharpen it up) and make it look better (without major redesign). I'd like to get the logo itself in all major file formats for print, web, etc.
Then I'd like a business card design that reflects a strategy consulting firm. It should be clean - logo and text without major graphics, and perhaps some small color treatments that match the logo color. The card should suggest high quality in terms of the company.
I'd like the files for card in all major print formats.
Target Market(s)
Silver Birch Partners is a strategy development and business consulting firm focused on small to mid-sized companies. We specialize in business strategy, comprehensive business plan development, market segmentation and positioning, financial models, marketing and sales strategy, product strategy and the effective use of social media in business growth. We operate as consultants, advisers, retained members of management teams, and Board members. We often serve in the role of Chief Strategy Officer, supporting CEO's and other senior executives to enhance top and bottom line growth.
Our overall approach with clients is to deliver actual results, and we often take an active team role with business founders and management teams to drive business growth and affect real changes in performance. As a result, we approach each situation uniquely and partner with clients in a manner that will have the biggest impact on enterprise value.
Industry/Entity Type
Business
Look and feel

```html
<!DOCTYPE html>
<html lang="en">
<head>
<meta charset="utf-8">
<title>Silver Birch Partners — Business Card</title>
<link rel="stylesheet" href="https://fonts.googleapis.com/css2?family=Jura:wght@500;600;700&display=swap">
<style>
  :root {
    --backdrop: #e4e5e8;
    --card-white: #ffffff;
    --card-shade: #eceef1;
    --charcoal: #3a3a3c;
    --navy: #2f3c6e;
    --ink: #2c2f38;
    --on-dark: #ffffff;
  }
  * { margin: 0; padding: 0; box-sizing: border-box; }
  html, body {
    width: 1200px; height: 901px; overflow: hidden;
    background: var(--backdrop);
    font-family: "Jura", "Eurostile", sans-serif;
  }
  .card {
    position: absolute; left: 150px; top: 193px;
    width: 900px; height: 514px;
    border-radius: 40px; overflow: hidden;
    background: linear-gradient(180deg, var(--card-white) 0%, var(--card-shade) 100%);
    box-shadow: 0 14px 36px rgba(0,0,0,0.18);
  }
  .card-shapes { position: absolute; inset: 0; width: 900px; height: 514px; }
  .brand {
    position: absolute; left: 150px; top: 78px;
    display: flex; align-items: center; gap: 18px;
  }
  .brand-dot { width: 26px; height: 26px; border-radius: 50%; background: var(--navy); }
  .brand-name {
    color: var(--ink); font-weight: 700; font-size: 30px;
    line-height: 1.08; letter-spacing: 1.5px; text-transform: uppercase;
  }
  .person { position: absolute; left: 150px; top: 222px; }
  .person-name {
    color: var(--ink); font-weight: 600; font-size: 32px;
    letter-spacing: 2px; text-transform: uppercase;
  }
  .person-role { color: var(--navy); font-weight: 600; font-size: 21px; margin-top: 2px; letter-spacing: 0.5px; }
  .contact {
    position: absolute; right: 34px; top: 282px;
    color: var(--on-dark); text-align: right; font-weight: 600;
  }
  .contact-address { font-size: 21px; line-height: 1.3; margin-right: 26px; }
  .contact-list { list-style: none; margin-top: 16px; font-size: 19px; }
  .contact-list li {
    display: flex; justify-content: flex-end; align-items: center;
    gap: 10px; height: 30px;
  }
  .contact-list svg { width: 16px; height: 16px; flex: none; }
</style>
</head>
<body>
  <article class="card">
    <svg class="card-shapes" viewBox="0 0 900 514" aria-hidden="true">
      <path class="accent-band" fill="var(--navy)"
            d="M0,268 C140,318 280,410 420,438 C300,432 150,380 0,322 Z"/>
      <path class="dark-base" fill="var(--charcoal)"
            d="M0,326 C150,392 300,452 430,450 C520,446 560,200 900,170 L900,514 L0,514 Z"/>
      <path class="light-rule" fill="none" stroke="var(--card-white)" stroke-width="5"
            d="M690,250 C760,215 830,200 900,195"/>
    </svg>

    <div class="brand">
      <span class="brand-dot"></span>
      <div class="brand-name">Silver Birch<br>Partners, LLC</div>
    </div>

    <div class="person">
      <div class="person-name">Daniel Harper</div>
      <div class="person-role">Managing Director</div>
    </div>

    <div class="contact">
      <div class="contact-address">214.9th floor.Plaza<br>Harbor Road BLK</div>
      <ul class="contact-list">
        <li>014 278 5361
          <svg viewBox="0 0 16 16"><path fill="#fff" d="M3 1l3 3-1.5 2c1 2 2.5 3.5 4.5 4.5L11 9l3 3-2 2.5C6 13 2.5 9.5 1 3z"/></svg>
        </li>
        <li>014 278 5361
          <svg viewBox="0 0 16 16"><rect x="4" y="1" width="8" height="14" rx="1.5" fill="none" stroke="#fff" stroke-width="1.6"/><circle cx="8" cy="12.5" r="0.9" fill="#fff"/></svg>
        </li>
        <li>014 278 5361
          <svg viewBox="0 0 16 16"><rect x="2" y="6" width="12" height="8" rx="1" fill="#fff"/><rect x="4" y="1.5" width="8" height="5" fill="none" stroke="#fff" stroke-width="1.4"/></svg>
        </li>
        <li>dharper@mail.com
          <svg viewBox="0 0 16 16"><rect x="1" y="3" width="14" height="10" rx="1" fill="#fff"/><path d="M1.5 3.5L8 9l6.5-5.5" fill="none" stroke="var(--charcoal)" stroke-width="1.2"/></svg>
        </li>
        <li>www.silverbirchco.com
          <svg viewBox="0 0 16 16"><g fill="none" stroke="#fff" stroke-width="1.3"><circle cx="8" cy="8" r="6.5"/><ellipse cx="8" cy="8" rx="3" ry="6.5"/><path d="M1.5 8h13M2.5 5h11M2.5 11h11"/></g></svg>
        </li>
      </ul>
    </div>
  </article>
</body>
</html>
```